Website Landing Page for Brightfall Systems

Create a custom designed website landing page for our business. Looking for a professional upscale design that incorporates our logo and logo colors into the theme. I want a standard fixed frame website, not a constant scrolling format that seems to be the trend. To start with I'm looking for more of the graphic design part, maybe a concept or theme, I don't expect to see a finished project. Not interested in generic templates or layouts.

The name of our company is Brightfall Systems and I've attached our logo below. I'd like to have the web page have the same look and feel of our logo, as well as the colors. Our company, Brightfall Systems does system design, installation, and programming, of residential and commercial Audio/Video and Automation systems. We do home theaters, lighting and building automation, video conferencing systems, security camera installations, conference rooms, projectors, distributed audio systems, and similar Technology projects. This will be a professional services/informational website. We will not sell products on this website. This website will be used to advertise our company and communicate our services to prospective customers. Having a well designed, professional and clean website is one way we want to distinguish our company from the competition.

Here are some examples of what I consider a professional well designed website
http://www.qorlamstudio.com/Work/

Last year we had our tradlo store designed (with PixelMarket) and I'm really happy with the way it turned out. You can see it at www.HolvenGearDepot.com I consider this to be a great design and looking for the same level of quality with this new website. However, do not copy or use any part of this design in this new project. This tradlo store is completely separate from our other company Brightfall Systems. I only mention this tradlo store an an example of good work.

Reason: Still going through designs.

Reason: Still working on project and have not had time to review all designs and request revisions.

Reason: Sill going through designs and requesting revisions

Reason: still going through all the submissions we received.

Target Market(s)

People interested in Audio/Video, home theaters, home automation. We do sales, system design, and programming. We typically work on larger projects with both residential and commercial customers.

Industry/Entity Type

Business

Number of Pages Required

1 page

Requirements
Must have
• Great design elements. Please use a white background. I think white goes well with our logo colors.

```html
<!DOCTYPE html>
<html lang="en">
<head>
<meta charset="utf-8">
<title>Brightfall Systems</title>
<link rel="stylesheet" href="https://fonts.googleapis.com/css2?family=Arimo:wght@700&family=Oswald:wght@400;500&display=swap">
<style>
  :root {
    --blue-deep: #3f7cbf;
    --blue-mid: #4d95d8;
    --blue-light: #5eaef0;
    --green: #6cc04a;
    --text-blue: #3d86d0;
    --nav-blue: #4f93da;
    --tel-blue: #b9dbf6;
    --white: #ffffff;
  }
  * { margin: 0; padding: 0; box-sizing: border-box; }
  html, body { width: 1200px; height: 1000px; overflow: hidden; background: var(--white); }
  .page { position: relative; width: 1200px; height: 1000px; font-family: "Arimo", Arial, sans-serif; }

  .top-band {
    position: absolute; left: 0; top: 0; width: 1200px; height: 118px;
    background: linear-gradient(to bottom, var(--blue-deep) 0%, var(--blue-mid) 30%, var(--blue-light) 50%, var(--blue-mid) 70%, var(--blue-deep) 95%);
    border-bottom: 4px solid var(--green);
    box-shadow: 0 4px 6px rgba(108,192,74,0.35);
  }
  .bottom-band {
    position: absolute; left: 0; top: 880px; width: 1200px; height: 120px;
    background: linear-gradient(to bottom, var(--blue-mid) 0%, var(--blue-light) 25%, var(--blue-mid) 60%, var(--blue-deep) 100%);
    border-top: 4px solid var(--green);
    box-shadow: 0 -4px 6px rgba(108,192,74,0.35);
  }

  .logo-box {
    position: absolute; left: 11px; top: 13px; width: 243px; height: 145px;
    background: var(--white);
    border: 3px solid var(--green);
    outline: 3px solid var(--blue-mid); outline-offset: -7px;
    display: flex; flex-direction: column; align-items: center; justify-content: center; gap: 12px;
  }
  .logo-dot { width: 60px; height: 60px; border-radius: 50%; background: var(--blue-mid); }
  .logo-name { font-family: "Oswald", sans-serif; font-weight: 500; font-size: 21px; letter-spacing: 1px; color: var(--blue-mid); text-transform: uppercase; }

  .tel { position: absolute; right: 36px; top: 82px; font-size: 17px; color: var(--tel-blue); }

  .main-nav { position: absolute; right: 19px; top: 132px; font-size: 18px; color: var(--nav-blue); }
  .main-nav a { color: var(--nav-blue); text-decoration: none; }
  .main-nav .sep { margin: 0 4px; }

  .intro { position: absolute; left: 0; top: 228px; width: 1200px; text-align: center; }
  .intro-title { font-family: "Oswald", sans-serif; font-weight: 400; font-size: 32px; letter-spacing: 1px; color: var(--blue-mid); text-transform: uppercase; line-height: 42px; }
  .intro-text { margin-top: 4px; font-size: 16px; line-height: 22px; color: var(--text-blue); }

  .hero {
    position: absolute; left: 90px; top: 378px; width: 1019px; height: 398px;
    background: linear-gradient(180deg, #1f4f9a 0%, #3a5f8a 30%, #b9875a 60%, #5d5a3c 85%, #2b2f22 100%);
  }
</style>
</head>
<body>
<div class="page">
  <header class="top-band"></header>
  <div class="logo-box">
    <span class="logo-dot"></span>
    <span class="logo-name">Brightfall Systems</span>
  </div>
  <div class="tel">TEL: 5550 2817 46</div>
  <nav class="main-nav">
    <a href="#">Home</a><span class="sep">|</span><a href="#">System</a><span class="sep">|</span><a href="#">Installation</a><span class="sep">|</span><a href="#">Programming</a><span class="sep">|</span><a href="#">Audio</a><span class="sep">|</span><a href="#">Video</a><span class="sep">|</span><a href="#">Automation</a><span class="sep">|</span><a href="#">Contact</a>
  </nav>

  <section class="intro">
    <h1 class="intro-title">Brightfall Systems</h1>
    <p class="intro-text">Does system design, installation, and programming, of residential and commercial Audio/Video and Automation systems.<br>We do home theaters, lighting and building automation, video conferencing systems, security camera installations,<br>conference rooms, projectors, distributed audio systems, and similar Technology projects.</p>
  </section>

  <div class="hero" role="img" aria-label="Photo of an upscale house with palm trees, lit at dusk"></div>

  <footer class="bottom-band"></footer>
</div>
</body>
</html>
```